Flowy subpage design wanted for a modern tax/accounting firm in Switzerland

--- Introduction ---
We are a tax and accounting firm in Switzerland. We provide services for expats living in Switzerland, our service is quite exclusive and modern (digital).

We just relaunched our website www.fiscaverde.ch and are happy with the design, so the desired subpage (more details below) should of course fit in.

--- Main brief ---
Please see Word File attached. The page has to include the whole text (11 chapters). A very intuitive, flowy design on only one subpage (not one page per chapter) is a MUST. Also, it is key that the design is supporting the content of the individual chapters, so it would be advantageous if you'd have a good unterstanding of the text attached.

--- Further information ---
A similar example would be this one: https://www2.brennmark.com/ch/en/pages/tax/articles/living-working-switzerland.html

This one is similar in what concerns the content, but NOT what we are looking for designwise. It is very simple and looks "thrown together", just not aesthetically pleasing in our opinion.

--- Final thoughts ---
- If you blow our minds with your design, we will certainly have future work for you.
- Our clients are between 20-50 years old, well educated, high income / high wealth, English speaking and living in Switzerland.
- CI/CD information:
Fonts
Montserrat regular / medium italic / bold
Colors
White #ffffffff
Darkblue #0a2b46
Darkblue 25% #b5bfc8
Darkblue 50% #8595a4
Greenblue #0d4261

We are looking forward to your designs!
Updates

Thank you very much for the submitted designs and your efforts. Unfortunately, none of the designs meet our expectations so far. Please note the following: - Designs that do not take CI into account will not be looked at more closely. - We have received many simple designs with very simple structure and accordion elements. But more important than the simple structure is an eye-catching design! Make it flowy and beautiful - We don't want pictures of Swiss vehicles, passes or other pictures that don't actively support the text. If you can make an illustration that really fits the context, fine, otherwise better leave it without. Thank you

Target Market(s)

Expats living in Switzerland. High income earners / high net worth individuals

Industry/Entity Type

tax/accounting

Number of Pages Required

1 page

Font styles to use
Other font styles liked:
• Montserrat

Colors
0054AA
0677BA
7BADD7
CADEEF
E8F1F8

Requirements
Must have
• based on general website design
Nice to have
• intuitive, flowy, attractive representation of much text
Should not have
• basic copy/paste of the text in sections :)

```html
<!DOCTYPE html>
<html lang="en">
<head>
<meta charset="utf-8">
<title>Living and working in Switzerland – Fiscaverde Advisory</title>
<link href="https://fonts.googleapis.com/css2?family=Montserrat:ital,wght@0,300;0,400;0,500;0,600;0,700;1,500&display=swap" rel="stylesheet">
<style>
:root{
  --white:#ffffff;
  --darkblue:#0a2b46;
  --greenblue:#0d4261;
  --db25:#b5bfc8;
  --db50:#8595a4;
  --accent:#2c5f8e;
  --accent-strong:#1f4f7c;
  --text:#6c7682;
  --line:#dfe5eb;
  --soft:#f3f6f9;
  --faint:#e8eef4;
}
*{box-sizing:border-box;margin:0;padding:0}
html,body{width:1200px;height:3026px;overflow:hidden;background:var(--white)}
body{position:relative;font-family:'Montserrat',sans-serif;color:var(--text)}
.abs{position:absolute}
p{font-size:11px;line-height:16px;color:var(--text)}

/* header */
.site-header{position:absolute;left:0;top:0;width:1200px;height:63px;background:var(--white)}
.brand{position:absolute;left:130px;top:12px;display:flex;align-items:center;gap:10px}
.brand-dot{width:40px;height:40px;border-radius:50%;background:var(--darkblue)}
.brand-name{font-size:17px;font-weight:600;line-height:19px;color:var(--darkblue);letter-spacing:.5px}
.main-nav{position:absolute;top:25px;left:449px;display:flex;gap:23px;font-size:12.5px;color:var(--accent)}
.main-nav .active{color:var(--darkblue);font-weight:600}
.caret{display:inline-block;border:4px solid transparent;border-top-color:var(--darkblue);margin-left:3px;vertical-align:1px}
.btn-calc{position:absolute;left:964px;top:18px;width:104px;height:31px;background:var(--darkblue);color:var(--white);font-size:12px;display:flex;align-items:center;gap:8px;padding-left:12px}

/* hero */
.hero{position:absolute;left:0;top:63px;width:1200px;height:369px;overflow:hidden;background:linear-gradient(100deg,#15365a 0%,#1a3d62 45%,#10304f 75%,#15395d 100%)}
.hero-city{position:absolute;right:0;top:0;width:520px;height:369px;background:linear-gradient(90deg,rgba(15,40,66,0) 0%,rgba(10,32,56,.7) 60%,rgba(22,55,88,.4) 100%)}
.hero-wedge{position:absolute;left:0;bottom:0}
.hero h1{position:absolute;left:143px;top:80px;font-size:44px;font-weight:400;line-height:48px;color:var(--white)}
.hero p{position:absolute;left:144px;top:200px;width:540px;font-size:11.5px;line-height:21.5px;color:#dce5ee}

/* breadcrumb */
.crumbs{position:absolute;left:0;top:432px;width:1114px;height:51px;border-bottom:1px solid #eceff3}
.crumbs .trail{position:absolute;left:143px;top:20px;font-size:10.5px;color:var(--accent)}
.crumbs .trail span{margin:0 8px;color:var(--darkblue)}
.burger{position:absolute;left:998px;top:20px;width:18px}
.burger i{display:block;height:1.5px;background:var(--accent);margin-bottom:4px}

/* section titles */
.sec-title{position:absolute;left:0;width:1200px;text-align:center;font-size:32px;font-weight:300;color:var(--accent);line-height:38px}
.sec-num{position:absolute;font-weight:200;color:var(--faint);line-height:1}
.sec-intro{position:absolute;text-align:center;font-size:13px;line-height:21px;color:#7a8490}
.sec-bar{position:absolute;left:544px;top:693px;width:76px;height:4px;background:var(--greenblue)}

/* accordion content */
.group-title{position:absolute;font-size:20px;font-weight:400;color:var(--accent)}
.rule{position:absolute;height:1px;background:var(--line)}
.acc-title{position:absolute;font-size:13.5px;font-weight:600;color:var(--accent-strong)}
.acc-sign{position:absolute;font-size:15px;font-weight:600;color:var(--accent)}
.quote-box{position:absolute;left:519px;top:884px;width:225px;height:182px;background:linear-gradient(90deg,#dcecf7 0%,#eef6fc 60%,#e4f0f9 100%);overflow:hidden}
.quote-box .quote{position:absolute;left:25px;top:26px;width:120px;font-size:15px;line-height:19px;color:var(--greenblue)}
.quote-box .quote b{font-weight:600}
.flag{position:absolute;left:138px;top:14px;width:82px;height:168px;background:linear-gradient(180deg,#e8eef4 0%,#d63a3a 12%,#c42a2a 45%,#e8eef4 62%,#e9f2f9 100%);opacity:.85}
.denom{position:absolute;top:1221px;height:79px;background:var(--soft);font-size:10.5px;line-height:14px}
.denom .k{position:absolute;color:#4c5a68}
.denom .v{position:absolute;color:var(--db50)}
.denom .sep{position:absolute;top:8px;width:1px;height:63px;background:#e2e8ee}
.article-title{position:absolute;font-size:21px;font-weight:400;color:var(--accent)}
.more{position:absolute;font-size:9px;letter-spacing:1px;color:var(--accent)}
.more::after{content:"→";margin-left:8px;font-size:10px}

/* sidebar */
.side{position:absolute;left:807px;top:722px;width:236px;height:375px;border:1px solid #e3e8ee;background:var(--white)}
.side .head{position:absolute;left:20px;top:19px;font-size:12px;color:var(--accent)}
.side .min{position:absolute;right:16px;top:14px;font-size:15px;color:var(--accent)}
.side ul{position:absolute;left:20px;top:62px;list-style:none;width:190px}
.side li{position:relative;font-size:10.5px;line-height:14px;color:var(--accent);padding-left:20px;margin-bottom:15px}
.side li::before{content:"";position:absolute;left:2px;top:6px;width:3px;height:3px;border-radius:50%;background:var(--accent)}
.side li.on{font-weight:600;color:var(--accent-strong)}
.side .row{position:absolute;left:19px;width:200px;font-size:10.5px;color:var(--accent)}
.side .row b{position:absolute;right:0;font-weight:600}

.city-band{position:absolute;left:160px;top:2101px;width:888px;height:182px;background:linear-gradient(100deg,#3a434b 0%,#59636b 35%,#8e969c 55%,#5a646c 75%,#343d45 100%)}

.toc{position:absolute;left:826px;top:2613px;width:216px;height:170px;background:var(--white);border:1px solid #edf1f5;box-shadow:0 6px 14px rgba(10,43,70,.08)}
.toc div{height:40px;border-bottom:1px solid #edf1f5;font-size:10.5px;color:var(--accent);display:flex;align-items:center;padding-left:20px}
.toc div:last-child{border-bottom:none}
.toc div::before{content:"›";margin-right:14px;font-size:13px}
</style>
</head>
<body>

<header class="site-header">
  <div class="brand"><span class="brand-dot"></span><span class="brand-name">FISCAVERDE<br>ADVISORY</span></div>
  <nav class="main-nav">
    <span class="active">Home</span><span>Tax returns</span><span>More services<i class="caret"></i></span><span>Swiss tax guide</span><span>About us</span>
  </nav>
  <div class="btn-calc">
    <svg width="12" height="15" viewBox="0 0 12 15"><rect x="0.5" y="0.5" width="11" height="14" fill="none" stroke="#fff"/><rect x="2.5" y="2.5" width="7" height="3" fill="#fff"/><g fill="#fff"><rect x="2.5" y="7" width="2" height="2"/><rect x="5" y="7" width="2" height="2"/><rect x="7.5" y="7" width="2" height="2"/><rect x="2.5" y="10" width="2" height="2"/><rect x="5" y="10" width="2" height="2"/><rect x="7.5" y="10" width="2" height="2"/></g></svg>
    Calculate
  </div>
</header>

<section class="hero">
  <div class="hero-city" role="img" aria-label="Dusk city skyline with high-rise towers"></div>
  <svg class="hero-wedge" width="420" height="72" viewBox="0 0 420 72"><defs><linearGradient id="wedge" x1="0" x2="1"><stop offset="0" stop-color="#e3e9ef"/><stop offset=".6" stop-color="#c9d3dc"/><stop offset="1" stop-color="#1a3d62"/></linearGradient></defs><polygon points="0,0 420,72 0,72" fill="url(#wedge)"/></svg>
  <h1>Living and working<br>in Switzerland</h1>
  <p>Lorem ipsum dolor sit amet, consectetur adipisicing elit, sed do eiusmod tempor incididunt ut labore et dolore magna aliqua. Ut enim ad minim veniam, quis nostrud exercitation ullamco laboris.</p>
</section>

<div class="crumbs">
  <div class="trail">Home<span>›</span>Living amd working in switzerland</div>
  <div class="burger"><i></i><i></i><i></i></div>
</div>

<div class="sec-num" style="left:548px;top:512px;font-size:100px">1</div>
<h2 class="sec-title" style="top:550px">Life in Switzerland</h2>
<p class="sec-intro" style="left:200px;top:623px;width:760px">To give you a small impression of what to expect when living in Switzerland, we have put together some topics for you to make your new start in Switzerland as pleasant as possible.</p>
<div class="sec-bar"></div>

<!-- General -->
<h3 class="group-title" style="left:163px;top:735px">General</h3>
<div class="rule" style="left:160px;top:775px;width:592px"></div>

<div class="acc-title" style="left:163px;top:796px">4 official languages</div>
<div class="acc-sign" style="left:723px;top:789px">–</div>
<p class="abs" style="left:163px;top:836px;width:595px">Unlike many other countries in Europe, where there is usually only one official national language, Switzerland has four of them: German, French, Italian and Romansh.</p>
<div class="abs" style="left:163px;top:888px;width:345px">
  <p>The most widespread language is German, which is spoken mainly in central Switzerland and the cantons bordering Germany.</p>
  <p style="margin-top:7px">French dominates in the western part of Switzerland, and Italian in the southeastern part.</p>
  <p style="margin-top:7px">Rhaeto-Romanic is spoken by only a very small part of the total population in eastern Switzerland.</p>
  <p style="margin-top:7px">In each region, there are also different dialects in the various languages.</p>
</div>
<div class="quote-box">
  <div class="flag" role="img" aria-label="Swiss flag waving on a pole"></div>
  <div class="quote"><b>Official documents</b> are generally issued in German, French and Italian.</div>
</div>

<div class="rule" style="left:158px;top:1103px;width:593px"></div>
<div class="acc-title" style="left:161px;top:1133px">Currency and banking</div>
<div class="acc-sign" style="left:717px;top:1130px">–</div>
<p class="abs" style="left:161px;top:1168px;width:595px">The national currency in Switzerland is the Swiss franc (CHF). 1 Swiss franc (Franken) is equal to 100 centimes (Rappen).</p>
<div class="denom" style="left:157px;width:300px">
  <span class="k" style="left:21px;top:19px;width:115px">The banknotes are available in the following amounts:</span>
  <span class="sep" style="left:146px"></span>
  <span class="v" style="left:173px;top:27px">10, 20, 50, 100,<br>200, 1000.</span>
</div>
<div class="denom" style="left:468px;width:275px">
  <span class="k" style="left:23px;top:20px;width:115px">For coins, there are the following denominations:</span>
  <span class="v" style="left:162px;top:27px">CHF 1, 2, 5<br>10, 20, 50 centimes</span>
</div>
<p class="abs" style="left:161px;top:1318px;width:595px">Current accounts can be opened at any major bank, Swiss Postalbank, cantonal or private banks. The largest banks in Switzerland are: Alpenbank, Helvia Bank and Postalis Finance.</p>

<div class="rule" style="left:160px;top:1374px;width:598px"></div>
<div class="acc-title" style="left:161px;top:1395px">Public holidays</div><div class="acc-sign" style="left:724px;top:1392px">+</div>
<div class="rule" style="left:160px;top:1428px;width:598px"></div>
<div class="acc-title" style="left:161px;top:1449px">Usual business and store opening hours</div><div class="acc-sign" style="left:724px;top:1446px">+</div>
<div class="rule" style="left:160px;top:1482px;width:598px"></div>
<div class="acc-title" style="left:161px;top:1501px">Electricity and water</div><div class="acc-sign" style="left:724px;top:1498px">+</div>
<div class="rule" style="left:160px;top:1536px;width:598px"></div>
<div class="acc-title" style="left:162px;top:1555px">Telephone and television</div><div class="acc-sign" style="left:724px;top:1552px">+</div>
<div class="rule" style="left:160px;top:1590px;width:598px"></div>

<h3 class="article-title" style="left:162px;top:1622px">Living in Switzerland</h3>
<p class="abs" style="left:162px;top:1676px;width:598px">The Swiss housing and real estate market varies greatly from region to region in terms of purchase and rental prices. In highly sought-after areas or larger cities, prices are relatively high, while living in rural areas is less expensive.</p>
<span class="more" style="left:164px;top:1745px">READ MORE</span>

<h3 class="article-title" style="left:162px;top:1792px">The education system in Switzerland</h3>
<p class="abs" style="left:162px;top:1853px;width:598px">In Switzerland, there are both public and private schools. The public schools are financed by the cantons and attendance at such a school is free of charge.</p>
<span class="more" style="left:163px;top:1904px">READ MORE</span>

<h3 class="article-title" style="left:159px;top:1948px">The healthcare system in Switzerland</h3>
<p class="abs" style="left:161px;top:2004px;width:598px">The healthcare system in Switzerland is one of the best in the world. Even in less densely populated regions, the density of hospitals and doctors' offices is high, so that medical care is always timely manner.</p>
<span class="more" style="left:162px;top:2050px">READ MORE</span>

<!-- sidebar -->
<aside class="side">
  <div class="head">General</div><div class="min">–</div>
  <div class="rule" style="left:0;top:45px;width:234px"></div>
  <ul>
    <li>4 official languages</li>
    <li class="on">Currency and banking</li>
    <li>Public holidays</li>
    <li>Usual business and store opening hours</li>
    <li>Electricity and water</li>
    <li>Telephone and television</li>
  </ul>
  <div class="rule" style="left:19px;top:252px;width:200px"></div>
  <div class="row" style="top:264px">Living in Switzerland<b>+</b></div>
  <div class="rule" style="left:19px;top:292px;width:200px"></div>
  <div class="row" style="top:304px">Driving in Switzerland<b>+</b></div>
  <div class="rule" style="left:19px;top:332px;width:200px"></div>
  <div class="row" style="top:344px">Public transport in Switzerland<b>+</b></div>
</aside>

<div class="city-band" role="img" aria-label="Aerial view of a city highway interchange beside office buildings"></div>

<!-- section 2 -->
<div class="sec-num" style="left:548px;top:2310px;font-size:170px">2</div>
<h2 class="sec-title" style="top:2360px">Switzerland - a brief overview of<br>the Alpine country</h2>
<p class="sec-intro" style="left:198px;top:2481px;width:806px;font-size:14px">Every year, Switzerland attracts many new citizens who want to settle there temporarily or long-term, and not without reason, because life in Switzerland is characterized by a high quality. If you are also thinking of settling here, we would like to introduce you to the country in the following.</p>

<h3 class="article-title" style="left:159px;top:2604px">A strong federation</h3>
<p class="abs" style="left:159px;top:2656px;width:600px">Switzerland is divided into 26 cantons, which have partial sovereignty and a capital. Together, the cantons form the Swiss Confederation - the federal state. The capital of the federal state is Bern. Unlike many other countries around the world, the political system in Switzerland is a direct democracy. The resulting autonomy as well as the willingness to compromise are deeply rooted in Swiss culture. Furthermore, neutrality in foreign policy issues is part of the self-image of Swiss politics.</p>

<h3 class="article-title" style="left:159px;top:2779px">A diverse population structure</h3>
<p class="abs" style="left:159px;top:2832px;width:600px">Many ethnicities and cultures meet in Switzerland. Of the total population of 8.6 million, one in four is a foreigner. Italians, Germans and Portuguese make up the largest proportion of expatriate Swiss. However, the number of non-European immigrants is growing steadily.</p>
<p class="abs" style="left:159px;top:2903px;width:600px">There are four official languages in Switzerland: German, French, Italian and Romansh. This alone shows that cultural identity here is based less on a common language or ethnic origin than on intercultural exchange.</p>

<nav class="toc">
  <div>A strong federation</div>
  <div>A diverse population structure</div>
  <div>High standard of living</div>
  <div>Exemplary pension system</div>
</nav>

</body>
</html>
```